Cover für Hauptkatalog
Zielgruppe
TESSARIN GmbH ist ein führender Großhändler in der Hobby- und Bastelbranche. mit unseren weit über 8.000 Produkten beliefern wir Einzelhändler in ganz Europa. Durch unsere Größe sind wir in der Lage sehr schnell auf individuelle Kundenwünsche zu reagieren.
Aufgabenstellung
Wir werden Mitte Dezember einen neuen Kreativ-Katalog mit über 450 Seiten unseren Kunden zur Verfügung stellen. In diesem Zusammenhang soll der Umschlag (Vorder- und Rückseite) in einem neuen, frischen Design erscheinen. Das aktuelle Layout kann unter www.tessarin-hobby.example eingesehen werden. Auf der Rückseite soll unsere Adresse stehen.

```html
<!DOCTYPE html>
<html lang="de">
<head>
<meta charset="utf-8">
<title>TESSARIN – Katalog Rückseite</title>
<link rel="stylesheet" href="https://fonts.googleapis.com/css2?family=Roboto:wght@400;700&display=swap">
<style>
  :root {
    --paper: #fefefe;
    --ink: #2b2b2b;
    --heading: #333333;
    --teal: #3aa7c9;
    --pink: #f1b6cc;
    --magenta: #c2268a;
    --mist: #eef0ee;
    --leaf: #a9c89a;
  }
  html, body {
    margin: 0;
    padding: 0;
    overflow: hidden;
  }
  body {
    width: 848px;
    height: 1200px;
    background: var(--paper);
    font-family: "Roboto", sans-serif;
    color: var(--ink);
    position: relative;
  }
  .hero-photo {
    position: absolute;
    left: 117px;
    top: 228px;
    width: 731px;
    height: 285px;
    background:
      radial-gradient(ellipse 18% 55% at 12% 45%, var(--leaf) 0%, rgba(169,200,154,0) 100%),
      radial-gradient(ellipse 24% 60% at 52% 55%, var(--teal) 0%, rgba(58,167,201,0) 100%),
      radial-gradient(ellipse 12% 28% at 53% 88%, var(--pink) 0%, rgba(241,182,204,0) 100%),
      radial-gradient(ellipse 12% 25% at 92% 20%, var(--magenta) 0%, rgba(194,38,138,0) 100%),
      radial-gradient(ellipse 12% 20% at 96% 90%, #e7609f 0%, rgba(231,96,159,0) 100%),
      linear-gradient(90deg, var(--mist) 0%, #f6f3f3 50%, #f3e4ee 100%);
  }
  .contact {
    position: absolute;
    right: 142px;
    text-align: right;
    white-space: nowrap;
    margin: 0;
  }
  .site-url {
    top: 560px;
    font-size: 19px;
    font-weight: 700;
    color: var(--heading);
    line-height: 24px;
  }
  .site-note {
    top: 582px;
    font-size: 13.5px;
    line-height: 18px;
  }
  .info-lines {
    top: 618px;
    font-size: 13.5px;
    line-height: 18.5px;
  }
  .office {
    position: absolute;
    top: 704px;
    text-align: right;
    white-space: nowrap;
  }
  .office--de { right: 347px; }
  .office--ch { right: 142px; }
  .office-name {
    margin: 0 0 6px;
    font-size: 19px;
    font-weight: 700;
    color: var(--heading);
    line-height: 24px;
  }
  .office-address {
    margin: 0;
    font-style: normal;
    font-size: 13.5px;
    line-height: 18.5px;
  }
</style>
</head>
<body>
  <div class="hero-photo" role="img" aria-label="Foto einer bunt bemalten Pappmaché-Eule in Türkis und Rosa mit Schmucksteinen, daneben pinke Windlichter vor hellem Fenster"></div>

  <p class="contact site-url">www.tessarin-hobby.example</p>
  <p class="contact site-note">NEUHEUTEN D | F | GB</p>

  <p class="contact info-lines">
    Weitere Informationen und Bezugsquellennachweis<br>
    Pour Toute information complemenaire et liste de revendeurs<br>
    Further information and documentation can be obtained from
  </p>

  <section class="office office--de">
    <h2 class="office-name">TESSARIN GmbH</h2>
    <address class="office-address">
      Lindenhofweg 9<br>
      79540 Lörrach<br>
      T. +49 7621 55 10-0<br>
      F. +49 7621 55 10 99<br>
      info@tessarin.example
    </address>
  </section>

  <section class="office office--ch">
    <h2 class="office-name">TESSARIN AG</h2>
    <address class="office-address">
      Seeblickweg 4<br>
      CH-4410 Liestal<br>
      T. +41 61 555 20 40<br>
      F. +41 61 555 20 41<br>
      info@tessarin-ch.example
    </address>
  </section>
</body>
</html>
```